Business Card Design - Furniture Retail

Open to both Single or double sided design

We are launching a online ecommerce store that sells Scandinavian/Danish style of furniture in Australia.

We aspire to provide stylish but classic and designers' selection of furniture to the Australia public at affordable price. For the style of the furniture we are selling, please see the following links:

https://www.filecrate.example/sh/qk3mzr8wlp/BXTpLnR4vQ7cYdHs?dl=0

The style of the design we are looking for is clean, simple that look Scandinavian/Danish but yet it is timeless classic.

Aspiring Design
http://www.lindmora.com
http://tobyquell.com.au/
http://vekt.furniture/
http://www.olvo.com/
Updates

Please display the card on normal angle for both front and back instead of funny angle. Please keep it display when displaying the design of the business cards so that we can focus on the designs rather than being confused by the unnecessary stuffs like the hands or background

I think there is already enough curve line on the logo itself so anything extra of the curve on the business card would be really unnecessary. Please avoid using any of the extra curve line on the business card, other than the logo itself. Thanks

Regular card and give them a matt celloglaze to create texture on card that makes it looked luxury and expensive.

Please display design on normal angle! Please only use white colour in the background (not the business card but the referring to the submission) rather than anything fancy so that we can focus on the design.

Target Market(s)

High end market consumers who are financially capable and who has good taste and appreciate good design

aged between 28 - 45 white collars professional/businessmen who live in metropolitan areas

Industry/Entity Type

Business

Font styles to use
Serif
Sans Serif

Requirements
Must have
• Regular card and give them a matt celloglaze to create texture on card that makes it looked luxury and expensive.

Please use the logo from the uploaded files

Company Name: Milo Verhagen
Name: Milo Reeb
Phone: +614 27 305 641
Website: www.miloverhagen.com.au
Email: milo@miloverhagen.com.au
Nice to have
• Colour is not limited to black and white
Should not have
• The concept photos of the furniture should NOT be used in the FRONT page of the business card.

```html
<!DOCTYPE html>
<html lang="en">
<head>
<meta charset="utf-8">
<title>Milo Verhagen – Business Card</title>
<link rel="stylesheet" href="https://fonts.googleapis.com/css2?family=Cinzel:wght@400&family=Open+Sans:wght@400&family=Kalam:wght@400&display=swap">
<style>
  :root {
    --page: #ffffff;
    --card: #ffffff;
    --ink: #0b0b0b;
    --paper-text: #ffffff;
    --contact: #3d4a55;
    --icon: #1a1a1a;
    --edge: #e4e4e4;
  }
  * { box-sizing: border-box; margin: 0; padding: 0; }
  html, body {
    width: 1200px; height: 900px; overflow: hidden;
    background: var(--page);
  }
  .card {
    position: absolute; left: 100px; top: 164px;
    width: 1000px; height: 571px;
    background: var(--card);
    border: 1px solid var(--edge);
    box-shadow: 0 6px 24px rgba(0,0,0,0.12);
    overflow: hidden;
  }
  .block { position: absolute; background: var(--ink); }
  .block--left   { left: 0;     top: 110px; width: 300px; height: 120px; }
  .block--middle { left: 300px; top: 40px;  width: 260px; height: 70px; }
  .block--right  { left: 560px; top: 30px;  width: 440px; height: 120px; }
  .bar--bottom-left  { left: 0;     top: 545px; width: 440px; height: 26px; }
  .bar--bottom-right { left: 560px; top: 452px; width: 440px; height: 20px; }

  .brand {
    position: absolute;
    font-family: 'Cinzel', serif;
    font-weight: 400;
    font-size: 17px;
    letter-spacing: 0.5px;
    white-space: nowrap;
  }
  .brand--left   { left: 30px;  top: 185px; color: var(--paper-text); }
  .brand--right  { left: 700px; top: 90px;  color: var(--paper-text); }
  .brand--middle {
    left: 340px; top: 160px; color: var(--ink);
    transform: rotate(180deg);
  }

  .holder-name {
    position: absolute; left: 170px; top: 285px;
    font-family: 'Kalam', cursive;
    font-size: 58px; color: var(--ink);
  }
  .contacts { position: absolute; left: 150px; top: 375px; list-style: none; }
  .contacts li {
    display: flex; align-items: center; gap: 14px;
    height: 40px;
    font-family: 'Open Sans', sans-serif;
    font-size: 19px; color: var(--contact);
  }
  .contacts li.contact--email { padding-left: 36px; }
  .contacts svg { width: 24px; height: 24px; flex: none; }
</style>
</head>
<body>
  <div class="card">
    <div class="block block--left"></div>
    <div class="block block--middle"></div>
    <div class="block block--right"></div>
    <div class="block bar--bottom-left"></div>
    <div class="block bar--bottom-right"></div>

    <span class="brand brand--left">MILO VERHAGEN</span>
    <span class="brand brand--middle">MILO VERHAGEN</span>
    <span class="brand brand--right">MILO VERHAGEN</span>

    <h1 class="holder-name">Milo Reeb</h1>

    <ul class="contacts">
      <li class="contact--phone">
        <svg viewBox="0 0 24 24" aria-hidden="true"><path fill="var(--icon)" d="M6.6 2.5l3 3.6-1.9 2.2c1.3 2.8 3.3 4.9 6 6.3l2.2-1.9 3.6 3-1.8 3.3c-7.6-.6-13.6-6.7-14.3-14.3z"/></svg>
        +614 27 305 641
      </li>
      <li class="contact--email">
        <svg viewBox="0 0 24 24" aria-hidden="true"><rect x="2" y="5" width="20" height="14" fill="none" stroke="var(--icon)" stroke-width="2"/><path d="M2 5l10 8 10-8M2 19l7.5-7M22 19l-7.5-7" fill="none" stroke="var(--icon)" stroke-width="1.6"/></svg>
        milo@miloverhagen.com.au
      </li>
      <li class="contact--web">
        <svg viewBox="0 0 24 24" aria-hidden="true"><circle cx="12" cy="12" r="10" fill="var(--icon)"/><g fill="none" stroke="#fff" stroke-width="1.2"><ellipse cx="12" cy="12" rx="4.2" ry="10"/><path d="M2 12h20M3.5 7h17M3.5 17h17M12 2v20"/></g></svg>
        www.miloverhagen.com.au
      </li>
    </ul>
  </div>
</body>
</html>
```